Web application layout remake

We are looking for a makeover on our web application called “QVRcrate” - it's a document management and digital archiving system integrating workflows and allowing you to free up physical space in your office currently occupied with documents by moving them to secure external custody.
We are expecting you to include the following:
• homepage
• signup page
• application page
This project is for the whole website (which is not big at all anyway!) and not just for the design of one page. The coding should be in HTML5 only.
We are aiming for fresh, appealing, clean, user friendly ,web 2.0, jquery layout.
Remakes or changes on the logo are welcome.
The application will be sold through the portal.
Please find in attachment the print screen of the application to aid you (this is the current view customers have after logging in but the layout is obsolete and we want a brand new!).
Reason: Still not happy with the received layouts. Keep up the good work! Thanks!
Reason: Still not happy with the whole solution and finding alternate app interfaces!
Digital

```html
<!DOCTYPE html>
<html lang="en">
<head>
<meta charset="utf-8">
<title>QVRcrate</title>
<link href="https://fonts.googleapis.com/css2?family=Source+Sans+3:wght@300;400;600&display=swap" rel="stylesheet">
<style>
:root{
  --navy:#062f66;
  --ink:#0b2d63;
  --link-blue:#1f63c8;
  --text:#333;
  --muted:#666;
  --rule:#cfcfcf;
  --panel:#f1f1f1;
  --bronze:#b0704a;
  --bronze-text:#a8653d;
  --silver:#b3b3b3;
  --silver-text:#9a9a9a;
  --gold:#e9b521;
  --gold-text:#e0a91a;
  --platinum:#dedede;
  --platinum-text:#aaa;
}
*{margin:0;padding:0;box-sizing:border-box}
html,body{width:1200px;height:1200px;overflow:hidden;background:#fff}
body{position:relative;font-family:"Source Sans 3",sans-serif;color:var(--text)}
.top-strip{position:absolute;left:0;top:0;width:1200px;height:15px;background:#000}
.bottom-strip{position:absolute;left:0;bottom:0;width:1200px;height:9px;background:#000}
.site-header{position:absolute;left:0;top:15px;width:1200px;height:112px;background:var(--navy)}
.brand{position:absolute;left:134px;top:38px;display:flex;align-items:center;gap:10px;color:#fff;font-size:38px;font-weight:400;line-height:1}
.brand-mark{width:30px;height:30px;background:#fff;border-radius:50%}
.main-nav{position:absolute;top:52px;left:0;width:1200px}
.main-nav a{position:absolute;color:#fff;text-decoration:none;font-size:20px;font-weight:300;white-space:nowrap}
.hero-photo{position:absolute;left:180px;top:135px;width:355px;height:495px;background:linear-gradient(180deg,#d8d8d8 0%,#eaeaea 60%,#f6f6f6 100%);border-radius:160px 160px 0 0}
.hero-rule{position:absolute;left:150px;top:629px;width:900px;height:2px;background:linear-gradient(90deg,transparent,#cfd3d8 20%,#cfd3d8 80%,transparent)}
.register{position:absolute;left:628px;top:170px;width:368px;height:432px;background:radial-gradient(circle at 50% 35%,#fafafa,#e8e8e8);border:1px solid #d6d6d6;box-shadow:0 2px 3px rgba(0,0,0,.2)}
.register h2{position:absolute;top:26px;left:0;width:100%;text-align:center;font-weight:400;font-size:37px;color:var(--ink);letter-spacing:-.5px}
.field{position:absolute;left:47px;width:269px;height:37px;background:#fff;border:1px solid #dcdcdc;border-radius:3px;font-size:15px;color:var(--ink);padding:9px 10px}
.submit{position:absolute;left:94px;top:274px;width:178px;height:43px;border-radius:3px;border:1px solid #0b3c8a;background:linear-gradient(#4f90e6,#1c5fc9 55%,#1650b4);color:#fff;font-size:17px;font-weight:300;text-align:center;line-height:41px}
.terms{position:absolute;left:0;top:336px;width:100%;text-align:center;font-size:14.5px;color:#555;line-height:17px;padding-left:12px}
.welcome-title{position:absolute;top:664px;left:105px;width:991px;display:flex;align-items:center;gap:8px}
.welcome-title::before,.welcome-title::after{content:"";flex:1;height:1px;background:var(--rule)}
.welcome-title h1{font-weight:300;font-size:33px;color:#333;letter-spacing:-.5px;line-height:40px}
.tagline{position:absolute;top:704px;width:1200px;text-align:center;font-size:17px;color:var(--link-blue)}
.intro{position:absolute;top:730px;left:100px;width:1000px;text-align:center;font-size:22px;font-weight:300;color:#222;line-height:25px}
.read-more{position:absolute;left:559px;top:797px;width:82px;height:32px;border:1px solid #0b3c8a;border-radius:4px;background:linear-gradient(#4f90e6,#1c5fc9);color:#fff;font-size:13px;font-weight:600;text-align:center;line-height:30px}
.section-rule{position:absolute;left:150px;width:900px;height:2px;background:linear-gradient(90deg,transparent,#dcdfe3 20%,#dcdfe3 80%,transparent)}
.plan{position:absolute;top:866px;width:222px;height:199px;border:1px solid #d9d9d9;background:#fff}
.plan-head{position:absolute;left:5px;top:6px;width:210px;height:65px;display:flex;justify-content:space-between;align-items:center;padding:0 14px 0 16px;color:#fff}
.plan-name{font-size:26px;font-weight:400}
.plan-price{font-size:43px;font-weight:400}
.plan-row{position:absolute;left:0;width:100%;text-align:center;font-size:19px;color:#444}
.plan-sep{position:absolute;left:4px;right:4px;top:106px;height:1px;background:#e4e4e4}
.plan-buy{position:absolute;left:0;bottom:0;width:100%;height:53px;background:var(--panel);text-align:center;line-height:53px;font-size:17px}
.bronze .plan-head{background:var(--bronze)} .bronze .plan-buy{color:var(--bronze-text)}
.silver .plan-head{background:var(--silver)} .silver .plan-buy{color:var(--silver-text)}
.gold .plan-head{background:var(--gold)} .gold .plan-buy{color:var(--gold-text)}
.platinum .plan-head{background:var(--platinum);padding:0 10px} .platinum .plan-buy{color:var(--platinum-text)}
.footer-links{position:absolute;left:113px;top:1121px;font-size:13px;color:#444;white-space:nowrap}
.footer-links span{margin:0 6px;color:#666}
.copyright{position:absolute;left:111px;top:1151px;font-size:12.5px;color:#444}
.social{position:absolute;left:941px;top:1124px}
</style>
</head>
<body>
<div class="top-strip"></div>

<header class="site-header">
  <div class="brand"><span class="brand-mark"></span>QVRcrate</div>
  <nav class="main-nav">
    <a style="left:470px">NEW STUFF</a>
    <a style="left:630px">PRICING</a>
    <a style="left:763px">60-DAY FREE TRIAL</a>
    <a style="left:980px">LOG IN</a>
  </nav>
</header>

<div class="hero-photo" role="img" aria-label="Black and white photo of a smiling businesswoman in a light blazer with arms crossed"></div>

<section class="register">
  <h2>REGISTER NOW</h2>
  <div class="field" style="top:81px">Your full name</div>
  <div class="field" style="top:128px">Company name</div>
  <div class="field" style="top:174px">Email</div>
  <div class="field" style="top:222px">Password</div>
  <div class="submit">CLICK TO SUBMIT</div>
  <p class="terms">By clicking you agree to the Terms of Service,<br>Privacy, and Refund policies.</p>
</section>

<div class="hero-rule"></div>

<div class="welcome-title"><h1>WELCOME TO QVR CRATE</h1></div>
<p class="tagline">YOUR TXT GOES HERE</p>
<p class="intro">Sed ut perspiciatis unde omnis iste natus error sit voluptatem accusantium doloremque laudantium,<br>totam rem aperiam, eaque ipsa quae ab illo inventore veritatis et quasi</p>
<div class="read-more">Read more</div>

<div class="section-rule" style="top:848px"></div>

<div class="plan bronze" style="left:120px">
  <div class="plan-head"><span class="plan-name">BRONZE</span><span class="plan-price">$39</span></div>
  <div class="plan-row" style="top:80px">›› 10 GB</div>
  <div class="plan-sep"></div>
  <div class="plan-row" style="top:110px">›› 10 USERS</div>
  <div class="plan-buy">BUY NOW!</div>
</div>
<div class="plan silver" style="left:366px">
  <div class="plan-head"><span class="plan-name">SILVER</span><span class="plan-price">$39</span></div>
  <div class="plan-row" style="top:80px">›› 25 GB</div>
  <div class="plan-sep"></div>
  <div class="plan-row" style="top:110px">›› 25 USERS</div>
  <div class="plan-buy">BUY NOW!</div>
</div>
<div class="plan gold" style="left:612px">
  <div class="plan-head"><span class="plan-name">GOLD</span><span class="plan-price">$39</span></div>
  <div class="plan-row" style="top:80px">›› 50 GB</div>
  <div class="plan-sep"></div>
  <div class="plan-row" style="top:110px">›› 50 USERS</div>
  <div class="plan-buy">BUY NOW!</div>
</div>
<div class="plan platinum" style="left:858px">
  <div class="plan-head"><span class="plan-name">PLATINUM</span><span class="plan-price">$39</span></div>
  <div class="plan-row" style="top:80px">›› 100 GB</div>
  <div class="plan-sep"></div>
  <div class="plan-row" style="top:110px">›› 100 USERS</div>
  <div class="plan-buy">BUY NOW!</div>
</div>

<div class="section-rule" style="top:1088px"></div>

<footer>
  <div class="footer-links">HELP<span>|</span>MOBILE<span>|</span>INTEGRATIONS<span>|</span>SECURITY<span>|</span>PRIVACY<span>|</span>TERMS<span>|</span>CONTACT</div>
  <p class="copyright">COPYRIGHT ©1999-2013 NORTHFIELD LABS, LLC. ALL RIGHTS RESERVED.</p>
  <svg class="social" width="120" height="28" viewBox="0 0 120 28" aria-hidden="true">
    <circle cx="14" cy="14" r="13" fill="#3b5b9e"/>
    <circle cx="44" cy="14" r="13" fill="#2a9fe0"/>
    <circle cx="74" cy="14" r="13" fill="#2a79c4"/>
    <circle cx="104" cy="14" r="13" fill="#d2392c"/>
  </svg>
</footer>

<div class="bottom-strip"></div>
</body>
</html>
```